Brochure Design

We need a 6 page Brochure designed for our product, please see attached document for more information. The content should focus on account work.

Target Market(s)

Businesses that use a taxi service for their business

Requirements
Must have
• Must have key content on the services we provide for Account work

```html
<!DOCTYPE html>
<html lang="en">
<head>
<meta charset="utf-8">
<title>Vexo Business Travel Brochure</title>
<link rel="stylesheet" href="https://fonts.googleapis.com/css2?family=Roboto:wght@400;500;700;900&display=swap">
<style>
  :root {
    --charcoal: #3a3a3b;
    --charcoal-deep: #2f2f30;
    --sun: #f0b323;
    --sun-deep: #dca01a;
    --paper: #ffffff;
    --mist: #bdbdbd;
    --backdrop: #e2e2e2;
    --sepia-light: #a8946a;
    --sepia-dark: #3f3a2f;
  }
  * { margin: 0; padding: 0; box-sizing: border-box; }
  html, body { width: 1200px; height: 900px; overflow: hidden; }
  body {
    background: var(--backdrop);
    font-family: "Roboto", Arial, sans-serif;
    position: relative;
  }
  .page {
    position: absolute;
    width: 380px;
    height: 380px;
    overflow: hidden;
    box-shadow: 0 6px 18px rgba(0,0,0,0.18);
  }
  .page svg.page-art { position: absolute; inset: 0; width: 100%; height: 100%; }
  .spread-left { left: 220px; top: 40px; background: var(--charcoal); }
  .spread-right { left: 600px; top: 40px; background: var(--sun); }
  .cover { left: 390px; top: 450px; width: 420px; height: 420px; background: var(--charcoal); }

  /* Inner left page */
  .why-block {
    position: absolute; left: 22px; top: 22px; width: 150px;
    color: var(--paper);
  }
  .section-title { font-size: 10px; font-weight: 700; margin-bottom: 6px; }
  .body-copy { font-size: 7px; line-height: 1.45; margin-bottom: 6px; color: #e6e6e6; }
  .accent-rule { width: 44px; height: 2px; background: var(--sun); margin: 10px 0 10px; }
  .safety-callout {
    position: absolute; left: 226px; top: 252px; width: 150px;
  }
  .safety-title {
    color: var(--sun); font-weight: 900; font-size: 13px; line-height: 1.1;
    text-transform: uppercase;
  }
  .safety-note {
    color: var(--charcoal); font-size: 11px; line-height: 1.2; margin-top: 6px; font-weight: 500;
  }

  /* Inner right page */
  .about-block {
    position: absolute; left: 24px; top: 246px; width: 330px;
    color: var(--charcoal-deep);
  }
  .about-title { font-size: 11px; font-weight: 900; margin-bottom: 5px; text-transform: uppercase; }
  .about-copy { font-size: 7.2px; line-height: 1.5; }

  /* Cover */
  .cover-rule {
    position: absolute; left: 120px; top: 196px; width: 70px; height: 4px; background: var(--sun);
  }
  .cover-headline {
    position: absolute; left: 82px; top: 212px; width: 200px;
    color: var(--paper); font-weight: 700; font-size: 22px; line-height: 1.12;
    text-transform: uppercase; letter-spacing: 0.5px;
  }
  .brand-mark {
    position: absolute; left: 274px; top: 270px; width: 80px; height: 80px;
    border-radius: 50%; background: var(--paper);
    display: flex; align-items: center; justify-content: center;
  }
  .brand-name {
    font-size: 20px; font-weight: 700; color: var(--charcoal);
  }
</style>
</head>
<body>

<section class="page spread-left" aria-label="Inner left page">
  <svg class="page-art" viewBox="0 0 380 380" aria-hidden="false">
    <defs>
      <linearGradient id="portraitTone" x1="0" y1="0" x2="1" y2="1">
        <stop offset="0" stop-color="var(--sepia-light)"/>
        <stop offset="1" stop-color="var(--sepia-dark)"/>
      </linearGradient>
    </defs>
    <circle cx="318" cy="150" r="140" fill="url(#portraitTone)" role="img" aria-label="Photo of a business traveller in a suit, sepia toned"/>
    <circle cx="318" cy="345" r="118" fill="var(--paper)"/>
  </svg>
  <div class="why-block">
    <h2 class="section-title">Why Choose Us</h2>
    <p class="body-copy">Our business account team has supported companies across the region for years, offering simple booking, clear monthly invoicing and priority pickups for staff and guests.</p>
    <p class="body-copy">Take full control of your travel spend, with every trip logged and easy to review online.</p>
    <p class="body-copy">Vexo with a dedicated account manager means you have access to 24/7 support should you need it.</p>
    <div class="accent-rule"></div>
    <h2 class="section-title">Our Success in Your Hands</h2>
    <p class="body-copy">We provide exceptional service for every journey, from airport runs to client visits, with fixed fares and drivers trained to represent your business well. Earn loyalty from your team, and please all the people all the time.</p>
  </div>
  <div class="safety-callout">
    <p class="safety-title">Your safety<br>is our priority</p>
    <p class="safety-note">Only vetted licensed drivers used by Vexo.</p>
  </div>
</section>

<section class="page spread-right" aria-label="Inner right page">
  <svg class="page-art" viewBox="0 0 380 380">
    <defs>
      <linearGradient id="cityTone" x1="0" y1="0" x2="0" y2="1">
        <stop offset="0" stop-color="#6e6350"/>
        <stop offset="0.55" stop-color="#a79672"/>
        <stop offset="1" stop-color="#d8cdb0"/>
      </linearGradient>
    </defs>
    <rect x="0" y="0" width="380" height="120" fill="var(--mist)"/>
    <path d="M0 120 Q 60 210 190 228 Q 320 210 380 120 L380 0 L380 380 L0 380 Z" fill="var(--sun)"/>
    <circle cx="200" cy="70" r="158" fill="var(--paper)"/>
    <circle cx="200" cy="70" r="150" fill="url(#cityTone)" role="img" aria-label="Photo of a city street lined with tall office towers, sepia toned"/>
  </svg>
  <div class="about-block">
    <h2 class="about-title">About Us</h2>
    <p class="about-copy">Vexo has been operational for the past 7 seven years operating under Vexo Tech Ltd since Dec 2014 (prior to that the company was operating under Rova Cars Ltd trading as Rova). Vexo has grown since the launch of Vexo starting in UK, followed by Ireland and the Scandinavian countries with the rest joining as popularity grew. Vexo has been the second largest taxi hailing company in Europe for the last 3 years.</p>
  </div>
</section>

<section class="page cover" aria-label="Front cover">
  <svg class="page-art" viewBox="0 0 420 420">
    <defs>
      <linearGradient id="travellerTone" x1="0" y1="0" x2="1" y2="1">
        <stop offset="0" stop-color="#b5a37c"/>
        <stop offset="1" stop-color="#4a4234"/>
      </linearGradient>
    </defs>
    <circle cx="220" cy="205" r="245" fill="var(--sun)"/>
    <path d="M420 300 Q 360 420 250 420 L420 420 Z" fill="var(--charcoal)"/>
    <circle cx="262" cy="128" r="124" fill="var(--mist)"/>
    <circle cx="262" cy="128" r="116" fill="url(#travellerTone)" role="img" aria-label="Photo of a smiling businesswoman holding a phone in the city, sepia toned"/>
    <circle cx="150" cy="282" r="132" fill="var(--charcoal)"/>
  </svg>
  <div class="cover-rule"></div>
  <h1 class="cover-headline">Exceptional travel for a modern business</h1>
  <div class="brand-mark"><span class="brand-name">vexo</span></div>
</section>

</body>
</html>
```